Sign Front of Business

Sign for front of workshop. We want Tolvar Mechanical in same font and colour as logo then the logo after name. Would like a background colour maybe dark blue with a border.

Target Market(s)

Mining Community

Industry/Entity Type

Mechanical

Requirements
Must have
• Logo colours

```html
<!DOCTYPE html>
<html lang="en">
<head>
<meta charset="utf-8">
<title>Tolvar Mechanical – Shopfront Sign</title>
<link rel="stylesheet" href="https://fonts.googleapis.com/css2?family=Exo+2:ital,wght@0,800;1,900&display=swap">
<style>
  :root {
    --page: #ffffff;
    --frame-light: #f4f5f7;
    --frame-mid: #c9ccd2;
    --frame-dark: #8d929b;
    --trim-red: #b3121f;
    --panel-deep: #0c2463;
    --panel-mid: #17388f;
    --gear-tone: #2553b5;
    --name-blue-light: #6fb4ff;
    --name-blue: #1f6fe0;
    --name-blue-dark: #0d3f9e;
    --chrome-light: #ffffff;
    --chrome-mid: #d9dce2;
    --chrome-dark: #7c828c;
    --mark-blue: #2a78e4;
    --mark-text: #ffffff;
  }

  * { box-sizing: border-box; margin: 0; padding: 0; }

  html, body {
    width: 1200px;
    height: 735px;
    overflow: hidden;
    background: var(--page);
  }

  .canvas {
    position: relative;
    width: 1200px;
    height: 735px;
    display: flex;
    align-items: center;
    justify-content: center;
  }

  .sign {
    width: 1160px;
    height: 176px;
    padding: 11px;
    background: linear-gradient(90deg,
      var(--frame-dark) 0%, var(--frame-light) 12%, var(--frame-mid) 30%,
      var(--frame-light) 48%, var(--frame-dark) 62%, var(--frame-light) 80%,
      var(--frame-mid) 100%);
    box-shadow: 0 3px 8px rgba(0, 0, 0, 0.25);
  }

  .sign-panel {
    position: relative;
    width: 100%;
    height: 100%;
    border: 2px solid var(--trim-red);
    overflow: hidden;
    display: flex;
    align-items: center;
    padding: 0 40px 0 58px;
  }

  .panel-backdrop {
    position: absolute;
    inset: 0;
    background:
      radial-gradient(ellipse at 8% 30%, var(--gear-tone) 0%, transparent 35%),
      radial-gradient(ellipse at 95% 40%, var(--gear-tone) 0%, transparent 30%),
      linear-gradient(90deg, var(--panel-mid), var(--panel-deep) 55%, var(--panel-mid));
    opacity: 0.95;
  }

  .business-name {
    position: relative;
    font-family: "Exo 2", sans-serif;
    font-style: italic;
    font-weight: 900;
    font-size: 66px;
    letter-spacing: -1px;
    line-height: 1;
    white-space: nowrap;
    text-transform: uppercase;
    filter: drop-shadow(2px 3px 0 rgba(0, 0, 0, 0.55));
  }

  .business-name .name-lead {
    background: linear-gradient(180deg, var(--name-blue-light) 0%, var(--name-blue) 50%, var(--name-blue-dark) 100%);
    -webkit-background-clip: text;
    background-clip: text;
    color: transparent;
    margin-right: 16px;
  }

  .business-name .name-trade {
    background: linear-gradient(180deg, var(--chrome-light) 0%, var(--chrome-mid) 48%, var(--chrome-dark) 52%, var(--chrome-light) 100%);
    -webkit-background-clip: text;
    background-clip: text;
    color: transparent;
  }

  .brand-mark {
    position: relative;
    margin-left: auto;
    display: flex;
    align-items: center;
    gap: 14px;
  }

  .brand-mark svg { display: block; }

  .brand-mark-name {
    font-family: "Exo 2", sans-serif;
    font-weight: 800;
    font-size: 26px;
    line-height: 1.05;
    color: var(--mark-text);
    width: 150px;
  }
</style>
</head>
<body>
  <main class="canvas">
    <section class="sign" aria-label="Tolvar Mechanical shopfront sign">
      <div class="sign-panel">
        <div class="panel-backdrop" role="img" aria-label="Dark blue background with faint scattered gear pattern"></div>

        <h1 class="business-name">
          <span class="name-lead">Tolvar</span><span class="name-trade">Mechanical</span>
        </h1>

        <div class="brand-mark">
          <svg width="86" height="86" viewBox="0 0 86 86" aria-hidden="true">
            <circle cx="43" cy="43" r="40" fill="var(--mark-blue)"/>
          </svg>
          <span class="brand-mark-name">Tolvar Mechanical</span>
        </div>
      </div>
    </section>
  </main>
</body>
</html>
```